New design for Hunting and Fishing trophy website

This project is for a psd (no coding) landing page plus one additional page for our company. GlintMount makes laser cut hunting and fishing trophies using customer's photographs. We want customers to understand our product at a glance and know they can order online easily from their smartphone or computer.

There should be a clear call to action that encourages visitors to continue on and place an order.

The site should perform well on smartphones as well as computers.

I am attaching our latest concept website. Please use it only to get background on our company and to see what we are trying to communicate to the visitors. We came up with this design on our own but want something clearer and more effective and probably entirely different.

You can also visit our current (ugly and ineffective) site at www.glintmount-example.com to learn more about our company and product.

The second page is our Trailhead Circle which is for outfitters and guides to promote their business by making their customers' experience more memorable by ordering GlintMounts for them. I'm attaching a psd of a really bad website mock-up of the Guide Page (again, we're looking for something much nicer and less wordy).

I've uploaded a couple extra before and after photos, and another photo of a trophy room. Our goal is for customers to start their own trophy room using GlintMounts. You don't need to use this photo (but you can), it's blurry. It helps you understand what we are trying to accomplish.

Of course, this site should appeal to hunting and fishing customers. Please be creative and help us succeed in this new business.

Target Market(s)

Hunting and Fishing sportsmen/women and people giving gifts to fellow hunters/fishers

Industry/Entity Type

Hunting

Number of Pages Required

2 page

Requirements
Must have
• Hunting and fishing feel.
• Clear call to action (we want orders). Our site will be set up so they can upload their photo, choose their text, and check out all in a few steps (we'll do this part).
• Communicate that we use their photo, You may want to use before and after images like I've uploaded.
Nice to have
• Our logo is in the psd files I've uploaded. That's the only element that must be on the new page (in addition to our product of course), but we're open to other logo styles if you want to suggest something that fits better with your design. Colors should look nice with our logo.
• Fast loading site, fonts that load fast are best.
• Our visitors may have just taken a photo of a fish or deer they are really proud of, and we want them to know we're a more accurate and affordable alternative to taxidermy that they can order right now using the photo they just took.
Should not have
• Too much going on. Most hunters are calm, nature lovers, so probably no bright flashy colors and busy graphics.

```html
<!DOCTYPE html>
<html lang="en">
<head>
<meta charset="utf-8">
<title>GlintMount – Custom Hunting and Fishing Trophies</title>
<link rel="stylesheet" href="https://fonts.googleapis.com/css2?family=Open+Sans:wght@400;600;700&family=Roboto+Slab:wght@400;700&family=Raleway:wght@400;500&display=swap">
<style>
  :root {
    --green: #0f9a5a;
    --green-dark: #0b7a45;
    --ink: #3d3d3d;
    --bar: #3c3c3c;
    --top-bg: #f3f3f3;
    --white: #ffffff;
    --line: #dddddd;
    --muted: #555555;
  }
  * { margin: 0; padding: 0; box-sizing: border-box; }
  html, body { width: 1200px; height: 1200px; overflow: hidden; background: var(--white); }
  body { position: relative; font-family: "Open Sans", sans-serif; color: var(--ink); }

  .site-header { position: absolute; top: 0; left: 0; width: 1200px; height: 100px; background: var(--top-bg); }
  .brand { position: absolute; left: 132px; top: 26px; display: flex; align-items: center; gap: 12px; font-size: 38px; font-weight: 700; color: var(--green); letter-spacing: -1px; }
  .brand-dot { width: 26px; height: 26px; border-radius: 50%; background: var(--green); }
  .call { position: absolute; right: 130px; top: 30px; font-size: 30px; font-weight: 600; color: var(--ink); }
  .call span { color: var(--green); }

  .main-nav { position: absolute; top: 100px; left: 0; width: 1200px; height: 50px; background: var(--bar); }
  .main-nav a { position: absolute; top: 5px; height: 40px; line-height: 40px; color: var(--white); text-decoration: none; font-size: 16px; }
  .main-nav .active { left: 130px; width: 100px; background: var(--green); text-align: center; font-weight: 600; }
  .cart { position: absolute; right: 130px; top: 14px; color: var(--white); font-size: 18px; }

  .hero-bg { position: absolute; top: 150px; left: 0; width: 1200px; height: 500px;
    background: radial-gradient(ellipse at 50% 40%, #d9b98f 0%, #b88a58 45%, #7a5530 100%); }
  .hero-title { position: absolute; top: 188px; left: 0; width: 1200px; text-align: center; color: var(--white); text-shadow: 0 2px 6px rgba(0,0,0,.35); }
  .hero-title .sub { display: block; font-size: 47px; font-weight: 400; line-height: 58px; padding-left: 118px; }
  .hero-title .main { display: block; font-size: 80px; font-weight: 600; line-height: 74px; padding-left: 122px; }

  .phone-photo { position: absolute; left: 213px; top: 338px; width: 215px; height: 454px; border-radius: 32px;
    background: linear-gradient(180deg, #7c8a8c 0%, #a7563a 45%, #5b4a3a 100%); }
  .trophy-photo { position: absolute; left: 738px; top: 345px; width: 318px; height: 450px;
    background: linear-gradient(180deg, #b56a4a 0%, #d65a2e 40%, #3f3127 80%, #111 100%); border-radius: 40px 40px 4px 4px; }

  .from-text { position: absolute; left: 450px; top: 500px; font-family: "Roboto Slab", serif; font-weight: 700; font-size: 29px; line-height: 36px; color: var(--white); text-shadow: 0 2px 4px rgba(0,0,0,.4); }
  .to-text { position: absolute; left: 610px; top: 802px; text-align: center; }
  .to-text strong { display: block; font-family: "Roboto Slab", serif; font-size: 20px; color: var(--green); }
  .to-text small { font-family: "Raleway", sans-serif; font-size: 15px; color: var(--muted); }

  .price { position: absolute; left: 211px; top: 888px; }
  .price .from { font-family: "Raleway", sans-serif; font-size: 26px; font-weight: 500; }
  .price .amount { font-family: "Roboto Slab", serif; font-size: 46px; font-weight: 700; color: var(--green); }
  .price .ship { font-family: "Roboto Slab", serif; font-size: 38px; font-weight: 700; display: block; line-height: 44px; }

  .order-frame { position: absolute; left: 692px; top: 905px; width: 297px; height: 94px; background: #d7d7d7; border-radius: 6px; padding: 7px; }
  .order-btn { display: block; width: 100%; height: 100%; background: linear-gradient(180deg, #14b26a, var(--green-dark)); color: var(--white); font-size: 30px; font-weight: 600; text-align: center; line-height: 80px; text-decoration: none; letter-spacing: .5px; }

  .site-footer { position: absolute; top: 1134px; left: 0; width: 1200px; height: 66px; border-top: 1px solid var(--line); font-size: 12px; color: var(--muted); }
  .copy { position: absolute; left: 131px; top: 26px; }
  .contact-line { position: absolute; right: 128px; top: 25px; display: flex; align-items: center; gap: 8px; }
  .contact-line svg { margin-left: 14px; }
</style>
</head>
<body>
  <header class="site-header">
    <div class="brand"><span>GlintMount</span><span class="brand-dot"></span></div>
    <div class="call">Call Us Now : <span>800-555-0142</span></div>
  </header>

  <nav class="main-nav">
    <a class="active" href="#">Home</a>
    <a style="left:288px" href="#">About Us</a>
    <a style="left:439px" href="#">Trailhead Circle</a>
    <a style="left:626px" href="#">F.A.Q</a>
    <a style="left:753px" href="#">Contact Us</a>
    <span class="cart">Cart : 0</span>
  </nav>

  <div class="hero-bg" role="img" aria-label="Blurred trophy room with shelves of laser-cut trophies"></div>

  <h1 class="hero-title">
    <span class="sub">Custom Hunting and Fishing Trophies</span>
    <span class="main">Made from your Photos!</span>
  </h1>

  <div class="phone-photo" role="img" aria-label="Smartphone showing a hunter's photo with his whitetail buck"></div>
  <div class="trophy-photo" role="img" aria-label="Finished laser-cut trophy of the hunter and buck on a black base with engraved text"></div>

  <p class="from-text">From your<br>PHONE,<br>CAMERA or<br>COMPUTER</p>

  <svg width="1200" height="1200" style="position:absolute;left:0;top:0;pointer-events:none" aria-hidden="true">
    <path d="M512 482 C600 420 720 430 785 495" fill="none" stroke="#fff" stroke-width="4"/>
    <path d="M725 492 L790 500 L752 462" fill="none" stroke="#fff" stroke-width="3"/>
    <path d="M700 858 C770 880 850 850 890 808" fill="none" stroke="#0f9a5a" stroke-width="3"/>
    <path d="M852 812 L893 804 L878 838" fill="none" stroke="#0f9a5a" stroke-width="2.5"/>
    <path d="M456 1048 C540 1100 650 1090 735 1028" fill="none" stroke="#0f9a5a" stroke-width="4"/>
    <path d="M668 1040 L737 1027 L705 1072" fill="none" stroke="#0f9a5a" stroke-width="3"/>
  </svg>

  <div class="to-text"><strong>To your Trophy</strong><small>(with free, optional text)</small></div>

  <div class="price">
    <span class="from">Starting at</span> <span class="amount">$ 39.95</span>
    <span class="ship">FREE SHIPPING!</span>
  </div>

  <div class="order-frame"><a class="order-btn" href="#">ORDER NOW !</a></div>

  <footer class="site-footer">
    <span class="copy">© Copyrights 2015. GlintMount</span>
    <div class="contact-line">
      <span>Get in Tech With Us :</span>
      <svg width="12" height="12" viewBox="0 0 24 24"><path d="M6 2l4 5-2 3c1 3 3 5 6 6l3-2 5 4-3 4C10 22 2 14 2 5z" fill="#555"/></svg>
      <span>800-555-0142</span>
      <svg width="14" height="11" viewBox="0 0 14 11"><rect width="14" height="11" rx="1" fill="#555"/><path d="M0 1 L7 6 L14 1" stroke="#fff" fill="none"/></svg>
      <span>contact@glintmount-example.com</span>
    </div>
  </footer>
</body>
</html>
```